Graphic designs required for HR consulting Website

We need to items designed to be used on our website and in presentations.
Please view our website for design ideas.
http://www.brightpeak.com.au.17.morvane.pw
See attached Powerpoint doc for more info.
InfoGraphic 1
Needs to be turned into an infographic that will be embedded into the BrightPeak HR website.
The fonts should be Helvetica Neue and should have the look and feel of the website.
InfoGraphic 2
Needs to be turned into an infographic that will be embedded into the BrightPeak HR website and used in PPT and WORD proposals.
The fonts should be Helvetica Neue, the look and
feel should be consistent with the first infographic.
A mountain analogy is needed that shows how the sequence of services will come together to take businesses on the journey to becoming great.
2 versions of the same information are shown on the following slides. The first is for ease of visibility, the second is to show the sequence of services on the journey.
Samples of possible design ideas for inspiration are at bottom of ppt.

```html
<!DOCTYPE html>
<html lang="en">
<head>
<meta charset="utf-8">
<title>People &amp; Performance Services</title>
<link rel="stylesheet" href="https://fonts.googleapis.com/css2?family=Inter:wght@300;400&display=swap">
<style>
  :root {
    --brand-blue: #2891d1;
    --navy: #06355a;
    --panel-light: #f0f2f3;
    --panel-grey: #dbe2e4;
    --ink: #1f2a30;
    --white: #ffffff;
  }
  * { box-sizing: border-box; margin: 0; padding: 0; }
  html, body {
    width: 1200px; height: 850px; overflow: hidden;
    background: var(--white);
    font-family: "Inter", "Helvetica Neue", Arial, sans-serif;
  }
  .infographic { position: relative; width: 1200px; height: 850px; }
  .column-title {
    position: absolute; top: 22px;
    color: var(--brand-blue); font-weight: 300;
    font-size: 38px; line-height: 47px; letter-spacing: -0.3px;
  }
  .column-title--needs { left: 52px; }
  .column-title--help { left: 756px; }

  .service-rows {
    position: absolute; left: 58px; top: 139px; width: 1093px;
    display: flex; flex-direction: column; gap: 5px;
  }
  .service-row {
    height: 221px;
    display: grid;
    grid-template-columns: 22px 510px 539px 22px;
    grid-template-rows: 86px 1fr;
  }
  .row-accent { grid-row: 1 / 3; background: var(--brand-blue); }
  .row-edge { grid-row: 1 / 3; grid-column: 4; background: var(--panel-grey); }

  .need-heading {
    grid-column: 2; grid-row: 1;
    background: var(--panel-light);
    color: var(--brand-blue); font-weight: 300;
    font-size: 35px; line-height: 34px; letter-spacing: -0.5px;
    padding: 0 20px 8px 30px;
    display: flex; align-items: flex-end;
  }
  .need-heading--spaced { padding-left: 28px; padding-bottom: 4px; }
  .need-detail {
    grid-column: 2; grid-row: 2;
    background: var(--panel-grey);
    color: var(--ink); font-size: 17.5px; line-height: 23.5px; font-weight: 400;
    padding: 24px 40px 0 30px;
  }

  .offer-heading {
    grid-column: 3; grid-row: 1;
    background: var(--brand-blue);
    color: var(--white); font-weight: 300;
    font-size: 35px; line-height: 34px; letter-spacing: -0.5px;
    padding: 0 20px 0 71px;
    display: flex; align-items: center;
  }
  .offer-heading--tall { align-items: flex-end; padding-bottom: 6px; }
  .offer-detail {
    grid-column: 3; grid-row: 2;
    position: relative;
    background: var(--navy);
    color: var(--brand-blue); font-size: 17px; font-weight: 300;
    padding: 24px 20px 0 71px;
  }
  .offer-detail p + p { margin-top: 13px; }
  .offer-pointer {
    position: absolute; left: 0; top: 44px;
    width: 31px; height: 59px;
  }
  .offer-pointer polygon { fill: var(--panel-grey); }
</style>
</head>
<body>
<main class="infographic">
  <h2 class="column-title column-title--needs">The people &amp; performance<br>needs of every business</h2>
  <h2 class="column-title column-title--help">How we can help you</h2>

  <section class="service-rows">
    <article class="service-row">
      <div class="row-accent"></div>
      <h3 class="need-heading">COMPLIANCE</h3>
      <p class="need-detail">Trusted advice on people issues including Fair Work Act compliance, redundancies, performance management, terminations, policies and safety.</p>
      <h3 class="offer-heading">HR ON-DEMAND</h3>
      <div class="offer-detail">
        <svg class="offer-pointer" viewBox="0 0 31 59" aria-hidden="true"><polygon points="0,0 31,29.5 0,59"/></svg>
        <p>Monthly subscription</p>
      </div>
      <div class="row-edge"></div>
    </article>

    <article class="service-row">
      <div class="row-accent"></div>
      <h3 class="need-heading">HR OPERATIONS</h3>
      <p class="need-detail">Operational HR support including recruitment, performance management and training.</p>
      <h3 class="offer-heading offer-heading--tall">ONSITE OR REMOTE<br>HR MANAGER</h3>
      <div class="offer-detail">
        <svg class="offer-pointer" viewBox="0 0 31 59" aria-hidden="true"><polygon points="0,0 31,29.5 0,59"/></svg>
        <p>Outsourced HR (annual subscription)</p>
        <p>OR adhoc HR support (fixed fee projects)</p>
      </div>
      <div class="row-edge"></div>
    </article>

    <article class="service-row">
      <div class="row-accent"></div>
      <h3 class="need-heading need-heading--spaced">PEOPLE &amp; PERFORMANCE<br>STRATEGY</h3>
      <p class="need-detail">Business strategy and planning, strategic HR frameworks and interventions to fuel your growth.</p>
      <h3 class="offer-heading offer-heading--tall">STRATEGIC EXPERTISE</h3>
      <div class="offer-detail">
        <svg class="offer-pointer" viewBox="0 0 31 59" aria-hidden="true"><polygon points="0,0 31,29.5 0,59"/></svg>
        <p>Fixed fee project based expertise</p>
      </div>
      <div class="row-edge"></div>
    </article>
  </section>
</main>
</body>
</html>
```